Webdesign mit Grundfarbe Weinrot für allgemeine Steuerberatung
Zielgruppe
Allgemeine Steuerberatung. Zielgruppe ist breit gefächert, allerdings soll die Webseite eher den Jungunternehmer ansprechen.
Aufgabenstellung
Die Grundfarbe sollte weinrot sein.

```html
<!DOCTYPE html>
<html lang="de">
<head>
<meta charset="utf-8">
<title>Steuerberatung Helene Varnow</title>
<link href="https://fonts.googleapis.com/css2?family=Outfit:wght@400;600&family=Source+Serif+4:wght@400;500&display=swap" rel="stylesheet">
<style>
  :root {
    --wine: #931100;
    --panel: #4a4a4a;
    --ink: #3c3c3c;
    --muted: #9a9a9a;
    --line: #cfcfcf;
    --soft: #eeeeee;
    --white: #ffffff;
    --sans: "Outfit", "Helvetica Neue", Arial, sans-serif;
    --serif: "Source Serif 4", Georgia, serif;
  }
  * { box-sizing: border-box; margin: 0; padding: 0; }
  html, body { width: 1200px; height: 2511px; overflow: hidden; }
  body { font-family: var(--serif); color: var(--ink); background: var(--white); }

  .hero { height: 667px; background: var(--wine); position: relative; color: var(--white); }
  .brand { position: absolute; left: 0; right: 0; top: 280px; text-align: center; }
  .brand-name { font-family: var(--serif); font-weight: 400; font-size: 64px; line-height: 1; letter-spacing: 0.5px; }
  .brand-role { font-family: var(--serif); font-weight: 400; font-size: 44px; margin-top: 14px; }
  .scroll-cue { position: absolute; left: 588px; top: 606px; }

  .feature { display: flex; height: 563px; }
  .feature-photo { width: 904px; height: 100%; background: linear-gradient(135deg, #2a2a2a 0%, #7c7c7c 45%, #c9c9c9 70%, #3a3a3a 100%); }
  .feature-side { flex: 1; background: var(--panel); padding: 32px 0 0 22px; display: flex; align-items: flex-start; gap: 16px; }
  .feature-side a { color: var(--white); text-decoration: none; font-family: var(--serif); font-weight: 500; font-size: 17px; line-height: 20px; }
  .feature-side svg { margin-top: 10px; }

  .services { padding: 63px 134px 0; height: 632px; }
  .section-title { font-family: var(--sans); font-weight: 600; font-size: 31px; line-height: 36px; }
  .section-title .accent { color: var(--wine); display: block; }
  .tabs { display: flex; margin-top: 48px; border-bottom: 2px solid var(--line); height: 56px; }
  .tab { font-family: var(--sans); font-size: 18px; color: var(--muted); display: flex; align-items: center; }
  .tab.active { color: var(--wine); font-weight: 600; width: 333px; border-top: 2px solid var(--line); border-right: 2px solid var(--line); margin-bottom: -2px; background: var(--white); }
  .tab.t2 { margin-left: 74px; }
  .tab.t3 { margin-left: auto; padding-right: 8px; }
  .service-body { display: flex; margin-top: 34px; }
  .service-list { width: 333px; border-right: 2px solid var(--line); list-style: none; height: 253px; }
  .service-list li { font-family: var(--sans); font-size: 19px; line-height: 33px; display: flex; align-items: center; gap: 10px; }
  .service-list li.current { color: var(--wine); }
  .service-detail { flex: 1; padding-left: 24px; }
  .service-detail h3 { font-family: var(--sans); font-weight: 600; font-size: 18px; color: var(--wine); margin-top: -3px; margin-bottom: 10px; }
  .service-detail ul { list-style: none; }
  .service-detail li { font-size: 12.6px; line-height: 21px; padding-left: 22px; position: relative; margin-bottom: 6px; }
  .service-detail li::before { content: "—"; position: absolute; left: 0; }

  .about { background: var(--soft); height: 270px; padding: 48px 134px 0; }
  .about p { font-size: 12.8px; line-height: 21px; margin-top: 26px; max-width: 930px; }

  .map { height: 298px; background: linear-gradient(160deg, #f2f2f2 0%, #e6e6e6 55%, #dcdcdc 100%); }

  .footer { height: 81px; background: var(--wine); color: var(--white); display: flex; align-items: center; padding: 0 104px 0 134px; font-family: var(--sans); font-size: 12.5px; }
  .footer nav { margin-left: auto; display: flex; gap: 55px; }
  .footer a { color: var(--white); text-decoration: none; }
</style>
</head>
<body>
  <header class="hero">
    <div class="brand">
      <div class="brand-name">Helene Varnow</div>
      <div class="brand-role">Steuerberaterin</div>
    </div>
    <svg class="scroll-cue" width="24" height="14" viewBox="0 0 24 14"><path d="M1 1 L12 12 L23 1" fill="none" stroke="#fff" stroke-width="2"/></svg>
  </header>

  <section class="feature">
    <div class="feature-photo" role="img" aria-label="Schwarzweißfoto: Beratungsgespräch am Schreibtisch mit Laptop und Unterlagen"></div>
    <aside class="feature-side">
      <svg width="10" height="18" viewBox="0 0 10 18"><path d="M1 1 L9 9 L1 17" fill="none" stroke="#fff" stroke-width="1.6"/></svg>
      <a href="#">Infothek und<br>Aktuelles</a>
    </aside>
  </section>

  <section class="services">
    <h2 class="section-title"><span class="accent">Leistungen</span>unserer Steuerberatungskanzlei</h2>
    <div class="tabs">
      <div class="tab active">Leistungen für Gewerbe &amp; Gründer</div>
      <div class="tab t2">Leistungen für Arbeitnehmer</div>
      <div class="tab t3">Sonstige Einkünfte</div>
    </div>
    <div class="service-body">
      <ul class="service-list">
        <li class="current"><svg width="7" height="12" viewBox="0 0 7 12"><path d="M1 1 L6 6 L1 11" fill="none" stroke="currentColor" stroke-width="1.5"/></svg>Buchhaltung</li>
        <li><svg width="7" height="12" viewBox="0 0 7 12"><path d="M1 1 L6 6 L1 11" fill="none" stroke="currentColor" stroke-width="1.5"/></svg>Lohnabrechnungen</li>
        <li><svg width="7" height="12" viewBox="0 0 7 12"><path d="M1 1 L6 6 L1 11" fill="none" stroke="currentColor" stroke-width="1.5"/></svg>Jahresabschluss</li>
        <li><svg width="7" height="12" viewBox="0 0 7 12"><path d="M1 1 L6 6 L1 11" fill="none" stroke="currentColor" stroke-width="1.5"/></svg>Steuererklärungen</li>
      </ul>
      <div class="service-detail">
        <h3>Buchhaltung für Selbstständige und Gewerbe</h3>
        <ul>
          <li>Wir kontieren und verbuchen Ihre Unterlagen und erstellen die Umsatzsteuervoranmeldungen und Betriebswirtschaftlichen Auswertungen. Dies schließt bei Bedarf die Offene-Posten-Buchhaltung und Anlagenbuchhaltung mit ein.</li>
          <li>Bei Lieferungen und sonstigen Leistungen innerhalb der Europäischen Gemeinschaft kümmern wir uns um die notwendige Zusammenfassende Meldung an das Zentralamt für Steuern.</li>
          <li>Sofern Ihre Buchhaltung als Jahresbuchhaltung (ohne monatliche oder vierteljährliche Umsatzsteuervoranmeldungen) von uns zu bearbeiten ist, unterstützen wir Sie natürlich auch bei Ihren Fragen während des Jahres.</li>
          <li>Wir leisten Hilfestellung für selbstbuchende Mandanten, helfen bei der Gestaltung des für Sie sinnvollen Kontenplanes und Fragen rund um die Verbuchung Ihrer Geschäftsvorfälle.</li>
        </ul>
      </div>
    </div>
  </section>

  <section class="about">
    <h2 class="section-title"><span class="accent">Über uns</span>Steuerberatung Varnow</h2>
    <p>Meine Kanzlei berät seit deren Gründung im Jahre 2003 Freiberufler, Gewerbetreibende, Kapitalgesellschaften, Personengesellschaften aus den verschiedensten Branchen sowie gemeinnützige Organisationen. Ebenso unterstützen wir gerne Existenzgründer und nebenberuflich Tätige, wie auch Arbeitnehmer, Vermieter und Rentner. Mein Team aus erfahrenen Steuerfachangestellten und ich freuen uns, Ihnen kompetent und individuell auf Ihre persönlichen Bedürfnisse abgestimmt, bei Ihren steuerlichen Angelegenheiten zu helfen.</p>
  </section>

  <div class="map" role="img" aria-label="Stadtplan mit Standort der Kanzlei"></div>

  <footer class="footer">
    <span>© 2019 - Steuerberatung Helene Varnow</span>
    <nav><a href="#">Datenschutz</a><a href="#">Impressum</a><a href="#">Kontakt</a></nav>
  </footer>
</body>
</html>
```